Coffee and Plastics

I am looking for a completely new site that shows the products we have. Our current site is www.velmorebrothersroast.com. We are open minded to what designers come up with. Our current site is www.velmorebrothersroast.com. You can you the information from there to start the site. I need these tabs on the main home page. ( Home, Coffee & Tea, Condiments, and Paper and Plastics, and Contact.) You can take photos and info from my Current site. In products page.
I will be uploading info and photo for paper and plastics.
Look and feel
Each slider illustrates characteristics of the customer's brand and the style your logo design should communicate.

```html
<!DOCTYPE html>
<html lang="en">
<head>
<meta charset="utf-8">
<title>Velmore Brothers Roast</title>
<link rel="stylesheet" href="https://fonts.googleapis.com/css2?family=Arimo:ital,wght@0,400;0,700;1,400&family=Lato:wght@300&display=swap">
<style>
  :root {
    --white: #ffffff;
    --brand-red: #6b1f10;
    --ink-dark: #3a2418;
    --hours: #6a5a7a;
    --nav: #3a1c14;
    --nav-active: #b08a6a;
    --band: #5c2412;
    --band-deep: #3f170c;
    --copy: #e8582c;
    --badge: #7a3a26;
    --badge-alt: #8f4a32;
  }
  * { margin: 0; padding: 0; box-sizing: border-box; }
  html, body { width: 1200px; height: 1010px; overflow: hidden; background: var(--white); }
  body { position: relative; font-family: "Arimo", Arial, sans-serif; }

  .hero-photo {
    position: absolute; left: 300px; top: 0; width: 900px; height: 526px;
    background: radial-gradient(ellipse at 70% 45%, #5a2c18 0%, #7a4226 30%, #c9a68e 60%, #ffffff 85%);
  }

  .brand { position: absolute; left: 52px; top: 48px; width: 200px; }
  .brand-name {
    font-weight: 700; font-size: 26px; line-height: 28px; color: var(--brand-red);
  }
  .contact-line { position: absolute; left: 52px; top: 158px; }
  .phone { font-weight: 700; font-size: 15px; color: var(--ink-dark); }
  .hours { font-size: 12px; color: var(--hours); margin-top: 3px; word-spacing: 2px; }

  .main-nav { position: absolute; left: 0; top: 500px; width: 1200px; height: 26px; }
  .main-nav a {
    position: absolute; top: 0; font-size: 17px; color: var(--nav); text-decoration: none;
  }
  .main-nav a.is-current { color: var(--nav-active); }

  .welcome {
    position: absolute; left: 0; top: 526px; width: 1200px; height: 364px; background: var(--band);
  }
  .welcome h1 {
    position: absolute; left: 46px; top: 18px; font-family: "Lato", sans-serif;
    font-weight: 300; font-size: 39px; color: var(--white);
  }
  .welcome-copy {
    position: absolute; left: 46px; top: 80px; width: 1066px; height: 190px;
    column-count: 2; column-gap: 26px; column-fill: auto;
    font-size: 15.5px; line-height: 19.5px; color: var(--copy);
  }
  .welcome-copy p { margin-bottom: 19.5px; }
  .guarantee {
    position: absolute; left: 46px; top: 278px; font-style: italic; font-size: 19px; color: var(--white);
  }
  .serving {
    position: absolute; left: 46px; top: 338px; font-size: 20px; color: var(--copy);
  }

  .partners {
    position: absolute; left: 0; top: 890px; width: 1200px; height: 120px; background: var(--band-deep);
  }
  .partner-badge { position: absolute; background: var(--badge); }
  .partner-badge.alt { background: var(--badge-alt); }
</style>
</head>
<body>
  <div class="hero-photo" role="img" aria-label="Close-up photograph of roasted coffee beans scattered on a white surface"></div>

  <header class="brand">
    <div class="brand-name">Velmore Brothers Roast</div>
  </header>

  <div class="contact-line">
    <div class="phone">1-800-555-0147</div>
    <div class="hours">MON-FRI &nbsp; 9 - 5 CENTRAL TIME</div>
  </div>

  <nav class="main-nav">
    <a href="#" style="left:44px">HOME</a>
    <a href="#" style="left:139px">TEA &amp; COFFEE</a>
    <a href="#" style="left:301px">CONDIMENTS</a>
    <a href="#" class="is-current" style="left:451px">PAPER &amp; PLASTICS</a>
    <a href="#" style="left:648px">CONTACT</a>
  </nav>

  <section class="welcome">
    <h1>Welcome to Velmore Brothers ROAST</h1>
    <div class="welcome-copy">
      <p>We are a family-owned and operated business based in Marlow Texas. Since the opening of Velmore Brothers Roast plant in 1995, we have become Texas’ premier independently owned coffee packaging company. Our success relies solely on the principle of selling only the freshest, highest-quality in-room coffee available.</p>
      <p>Velmore Brothers packages and supplies in-room coffee, tea products, and condiments. Whether we’re supplying a 50-room Hotel or a 500-room grand resort, we have the distribution capacity to fill your rooms with the most aromatic and robust coffees and teas available at competitive prices.</p>
      <p>Velmore Brothers is continuously striving for ways to improve quality and product appearance to meet the highest standards in today’s franchises and independent hotels. We are very aware that our success depends entirely upon maintaining our customers’ confidence in our products, so we pay close attention to your needs every step of the way.</p>
    </div>
    <p class="guarantee">We guarantee all of our products will meet your level of satisfaction.</p>
    <p class="serving">SERVING FINE ESTABLISHMENTS EVERYWHERE !</p>
  </section>

  <footer class="partners" aria-label="Partner hotels">
    <div class="partner-badge" style="left:46px;top:34px;width:88px;height:44px"></div>
    <div class="partner-badge alt" style="left:156px;top:34px;width:106px;height:42px"></div>
    <div class="partner-badge" style="left:288px;top:32px;width:84px;height:56px"></div>
    <div class="partner-badge alt" style="left:404px;top:36px;width:60px;height:66px"></div>
    <div class="partner-badge" style="left:493px;top:34px;width:67px;height:64px"></div>
    <div class="partner-badge alt" style="left:584px;top:34px;width:58px;height:66px"></div>
    <div class="partner-badge" style="left:674px;top:32px;width:63px;height:68px"></div>
    <div class="partner-badge alt" style="left:770px;top:34px;width:89px;height:44px"></div>
    <div class="partner-badge" style="left:881px;top:34px;width:105px;height:42px"></div>
    <div class="partner-badge alt" style="left:1013px;top:32px;width:84px;height:56px"></div>
  </footer>
</body>
</html>
```